Website design for learning and development business

I need a logo for my new business based in Australasia. I am a kiwi who is a creative change maker working in the Learning & development space. I design experiential learning opportunities for businesses to grow and nurture their tribes. I take a holistic look at an organisation and analyse what is needed to build a positive culture with a growth mindset woven into their DNA. I would like to see designs that are based on the following word snaps - creative, interesting, tribal, journey, adaptability, engaging, fluid, architectural, bespoke, courageous, challenging .I have the logo (attached) and I Need a startup business website designed. I am a Learning and development professional who is looking at going out on my own and establishing my own business. I would like a website designed that people would go to to check out what I do, how I do, what skills I have and how to contact me. Also room for a blog/articles.

Target Market(s)

Small to medium business

Industry/Entity Type

Self employed training and consultancy company

Number of Pages Required

5+ page

Requirements
Must have
• home page, about page, contact us page, blog page, search for us page
Nice to have
• Testimonials,

```html
<!DOCTYPE html>
<html lang="en">
<head>
<meta charset="utf-8">
<title>Verdant Consulting — Learning and Development Professional</title>
<link rel="stylesheet" href="https://fonts.googleapis.com/css2?family=Russo+One&family=Lato:wght@400;700;900&display=swap">
<style>
:root{
  --green:#3cad3a;
  --green-dark:#14361b;
  --green-deep:#0d2613;
  --red:#e02c35;
  --blue:#4394d6;
  --orange:#f0612a;
  --navy:#2b2f7a;
  --yellow:#c9c317;
  --ink:#1d1d1d;
  --grey:#555;
  --white:#fff;
  --black:#000;
}
*{margin:0;padding:0;box-sizing:border-box}
html,body{width:1200px;height:4368px;overflow:hidden}
body{position:relative;background:var(--white);font-family:"Lato",sans-serif;color:var(--ink)}
.abs{position:absolute}
.display{font-family:"Russo One",sans-serif;text-transform:uppercase}

/* header & hero */
.hero{left:0;top:0;width:1200px;height:771px;background:radial-gradient(ellipse at 60% 40%,#2b5a2c 0%,#1a3f1f 45%,var(--green-deep) 100%);overflow:hidden}
.brand{left:171px;top:70px;color:var(--white);font-family:"Russo One",sans-serif;line-height:1}
.brand-name{font-size:46px;letter-spacing:1px}
.brand-sub{font-size:16px;letter-spacing:9px;margin-top:6px;padding-left:40px}
.nav{left:551px;top:68px;display:flex;align-items:center;gap:0;font-weight:900;font-size:14px;color:var(--white)}
.nav a{color:var(--white);text-decoration:none;margin-right:28px}
.nav .nav-cta{background:var(--green);padding:16px 12px;border-radius:6px;margin-left:4px;margin-right:0}
.hero-title{left:171px;top:232px;color:var(--white);font-size:48px;line-height:63px}
.hero-title span{display:block}
.hero-title .small{font-size:38px}
.hero-photo{left:560px;top:170px;width:640px;height:420px;border-radius:50% 40% 45% 55%;background:radial-gradient(ellipse at 45% 40%,#c4d43a 0%,#6aa53a 40%,rgba(40,90,40,0) 75%)}
.hero-wave{left:0;top:600px;width:1200px;height:180px}

/* what i do */
.section-title{font-size:34px;color:var(--ink)}
.what-title{left:0;width:1200px;top:878px;text-align:center}
.service{top:976px;width:277px;height:312px;border-radius:10px;overflow:hidden}
.service .photo{height:230px}
.service .label{height:82px;display:flex;align-items:center;justify-content:center;text-align:center;color:var(--white);font-family:"Russo One",sans-serif;font-size:20px;line-height:28px;text-transform:uppercase}
.svc-1{left:171px}.svc-1 .photo{background:linear-gradient(135deg,#d9d9d9,#7d7c78 60%,#3a3a3c)}.svc-1 .label{background:var(--green)}
.svc-2{left:461px}.svc-2 .photo{background:linear-gradient(135deg,#c9b59f,#e6dfd6 50%,#d4a23a)}.svc-2 .label{background:var(--red)}
.svc-3{left:751px}.svc-3 .photo{background:linear-gradient(135deg,#a9c6e0,#ede9e4 50%,#6b7c92)}.svc-3 .label{background:var(--blue)}

/* how i do */
.how{left:0;top:1305px;width:1200px;height:865px;background:linear-gradient(100deg,#2a2c35 0%,#514b4f 30%,#c89a72 60%,#f1d7a3 80%,#c9a87c 100%);overflow:hidden}
.how::after{content:"";position:absolute;left:0;right:0;bottom:0;height:260px;background:linear-gradient(180deg,rgba(60,45,30,0),rgba(50,40,30,.85))}
.how-photo{left:0;top:0;width:1200px;height:865px}
.how-wave{left:0;top:0;width:1200px;height:300px;z-index:2}
.how-title{left:171px;top:370px;color:var(--white);font-size:32px;z-index:3}
.how-copy{left:171px;top:435px;width:370px;color:#f2f2f2;font-size:13.5px;line-height:27px;text-align:justify;z-index:3}
.btn{background:var(--green);color:var(--white);font-weight:900;font-size:14px;border-radius:7px;display:flex;align-items:center;justify-content:center;text-transform:uppercase}
.how-btn{left:171px;top:656px;width:110px;height:56px;z-index:3}

/* skills */
.skills-heading{left:72px;top:2575px;transform:rotate(-90deg);transform-origin:center;width:220px;margin-left:-80px;font-family:"Lato",sans-serif;font-weight:900;font-size:34px;color:var(--ink);text-align:center;white-space:nowrap}
.skills-arc{left:0;top:2200px;width:1200px;height:760px}
.skill{text-align:right;width:420px}
.skill h3{font-weight:400;font-size:24px;letter-spacing:.5px;text-transform:uppercase;color:var(--ink)}
.skill p{font-size:15px;color:var(--grey);margin-top:6px}
.skill-icon{width:76px;height:76px;border-radius:50%;display:flex;align-items:center;justify-content:center}
.person-photo{left:640px;top:2270px;width:420px;height:595px;background:linear-gradient(180deg,#f4f4f4 0%,#d8cfc6 25%,#8d7a6c 60%,#6d5e54 100%);border-radius:200px 200px 0 0}

/* blog */
.blog{left:0;top:2930px;width:1200px;height:904px;background:linear-gradient(180deg,#fff 0%,#eef1f0 40%,#e6ebe9 70%,#fff 100%)}
.blog-title{left:0;width:1200px;top:3065px;text-align:center}
.card{background:var(--white);border-radius:12px;overflow:hidden;box-shadow:0 6px 20px rgba(0,0,0,.12)}
.card-main{left:171px;top:3187px;width:554px;height:517px}
.card-main .photo{height:410px;background:linear-gradient(120deg,#cfd6dc 0%,#e9e2da 40%,#9aa6b2 100%)}
.card-main .meta{display:flex;padding:22px 20px 0 20px;gap:18px}
.date{text-align:center;font-weight:900;line-height:1}
.date .m{font-size:15px}
.date .d{font-size:34px;margin-top:4px}
.card-main h4{font-weight:900;font-size:14px;text-transform:uppercase;margin-top:2px}
.card-main p{font-size:11.5px;color:var(--grey);line-height:20px;margin-top:6px}
.card-side{left:751px;width:276px;height:245px}
.card-side .photo{height:178px}
.card-side .foot{display:flex;align-items:center;justify-content:space-between;padding:12px 16px 0 14px}
.card-side h4{font-weight:900;font-size:13.5px;line-height:21px;text-transform:uppercase;width:210px}
.side-1{top:3187px}.side-1 .photo{background:linear-gradient(135deg,#e1e6ea,#8f9ba8 60%,#4d5765)}
.side-2{top:3458px}.side-2 .photo{background:linear-gradient(135deg,#cfd7dd,#7a8a99 55%,#3e4752)}

/* footer */
.footer{left:0;top:3834px;width:1200px;height:534px;background:var(--black);color:var(--white)}
.contact-title{left:171px;top:3950px;font-size:26px;color:var(--white)}
.field{left:171px;width:270px;height:56px;background:var(--white);border-radius:9px;color:var(--ink);font-size:14px;display:flex;align-items:center;padding-left:12px}
.submit{left:171px;top:4141px;width:120px;height:54px}
.footer-brand{left:568px;top:4040px;width:460px;color:var(--white);font-family:"Russo One",sans-serif;text-align:center;line-height:1}
.footer-brand .brand-name{font-size:72px}
.footer-brand .brand-sub{font-size:24px;letter-spacing:14px;padding-left:0;margin-top:8px}
.footer-rule{left:171px;top:4271px;width:856px;height:1px;background:#666}
.copyright{left:0;width:1200px;top:4310px;text-align:center;font-size:13px;font-weight:700;color:var(--white)}
</style>
</head>
<body>

<!-- Hero -->
<section class="abs hero">
  <div class="abs hero-photo" role="img" aria-label="Photo of a colourful chameleon on a branch"></div>
  <div class="abs brand"><div class="brand-name">VERDANT</div><div class="brand-sub">CONSULTING</div></div>
  <nav class="abs nav">
    <a href="#">HOME</a><a href="#">ABOUT</a><a href="#">CONTACT US</a><a href="#">BLOG</a><a href="#" class="nav-cta">SEARCH FOR US</a>
  </nav>
  <h1 class="abs hero-title display"><span>Learning and</span><span class="small">Development</span><span class="small">Professional</span></h1>
  <svg class="abs hero-wave" viewBox="0 0 1200 180" preserveAspectRatio="none">
    <path d="M0,140 C60,70 160,20 320,40 C480,60 600,100 760,110 C900,120 1000,150 1080,150 L1200,171 L1200,180 L0,180 Z" fill="var(--green)"/>
    <path d="M0,150 C90,100 200,65 360,70 C520,75 620,95 780,110 C900,125 980,150 1060,145 C1120,142 1170,160 1200,171 L1200,180 L0,180 Z" fill="var(--white)"/>
  </svg>
</section>

<!-- What I do -->
<h2 class="abs section-title display what-title">What I do</h2>
<article class="abs service svc-1"><div class="photo" role="img" aria-label="Photo of a team at a customer service training session"></div><div class="label">Customer service<br>training</div></article>
<article class="abs service svc-2"><div class="photo" role="img" aria-label="Photo of a supportive conversation between colleagues"></div><div class="label">Mental health<br>awareness</div></article>
<article class="abs service svc-3"><div class="photo" role="img" aria-label="Photo of two colleagues with headsets talking"></div><div class="label">Policy<br>training</div></article>

<!-- How I do -->
<section class="abs how">
  <div class="abs how-photo" role="img" aria-label="Photo of a person standing in a grassy field at sunset with birds in the sky"></div>
  <svg class="abs how-wave" viewBox="0 0 1200 300" preserveAspectRatio="none">
    <path d="M80,0 C200,0 300,190 470,235 C620,275 720,215 860,185 C1000,155 1110,150 1200,175 L1200,0 Z" fill="var(--white)"/>
  </svg>
  <h2 class="abs section-title display how-title">How I do</h2>
  <p class="abs how-copy">Nam libero tempore, cum soluta nobis est eligendi optio cumque nihil impedit quo minus id quod maxime placeat facere possimus, omnis voluptas assumenda est, omnis dolor repellendus. Temporibus autem quibusdam et aut officiis debitis aut rerum necessitatibus saepe eveniet ut et voluptates repudiandae sint et molestiae non recusandae. Itaque earum rerum hic tenetur.</p>
  <a class="abs btn how-btn">Read more</a>
</section>

<!-- Skills -->
<h2 class="abs skills-heading">WHAT SKILLS I HAVE</h2>
<svg class="abs skills-arc" viewBox="0 0 1200 760">
  <path d="M810,40 C600,60 480,230 505,380 C530,560 650,700 810,715" fill="none" stroke="var(--green)" stroke-width="8"/>
</svg>
<div class="abs person-photo" role="img" aria-label="Photo of a cheerful man in glasses and a checked blazer"></div>

<div class="abs skill" style="left:136px;top:2290px"><h3>Creative</h3><p>Nam libero tempore, cum soluta nobis</p></div>
<div class="abs skill-icon" style="left:572px;top:2284px;background:var(--orange)"><svg width="36" height="36" viewBox="0 0 36 36" fill="none" stroke="#fff" stroke-width="2.4"><circle cx="18" cy="16" r="8"/><path d="M14 27h8M15 31h6M18 3v3M6 16H3M33 16h-3M9 7l2 2M27 7l-2 2"/></svg></div>

<div class="abs skill" style="left:68px;top:2388px"><h3>Interesting</h3><p>Nam libero tempore, cum soluta nobis</p></div>
<div class="abs skill-icon" style="left:506px;top:2381px;background:var(--red)"><svg width="36" height="36" viewBox="0 0 36 36" fill="none" stroke="#fff" stroke-width="2.4"><path d="M6 8h24v16H14l-6 5v-5H6z"/><path d="M13 14v4M21 14v4"/></svg></div>

<div class="abs skill" style="left:36px;top:2494px"><h3>Tribal</h3><p>Nam libero tempore, cum soluta nobis</p></div>
<div class="abs skill-icon" style="left:472px;top:2488px;background:var(--navy)"><svg width="36" height="36" viewBox="0 0 36 36" fill="none" stroke="#fff" stroke-width="2.4"><circle cx="18" cy="16" r="4"/><path d="M11 30c0-5 3-8 7-8s7 3 7 8M5 27c0-4 2-6 5-6M31 27c0-4-2-6-5-6M18 4v5M12 7l2 3M24 7l-2 3"/></svg></div>

<div class="abs skill" style="left:41px;top:2607px"><h3>Journey</h3><p>Nam libero tempore, cum soluta nobis</p></div>
<div class="abs skill-icon" style="left:479px;top:2598px;background:var(--blue)"><svg width="36" height="36" viewBox="0 0 36 36" fill="none" stroke="#fff" stroke-width="2.4"><path d="M10 6a5 5 0 0 1 5 5c0 4-5 9-5 9s-5-5-5-9a5 5 0 0 1 5-5z"/><path d="M26 16a4 4 0 0 1 4 4c0 3-4 7-4 7s-4-4-4-7a4 4 0 0 1 4-4z"/><path d="M10 24c0 6 10 6 12 4" stroke-dasharray="2 3"/></svg></div>

<div class="abs skill" style="left:73px;top:2712px"><h3>Adaptability</h3><p>Nam libero tempore, cum soluta nobis</p></div>
<div class="abs skill-icon" style="left:509px;top:2703px;background:var(--yellow)"><svg width="36" height="36" viewBox="0 0 36 36" fill="none" stroke="#fff" stroke-width="2.4"><rect x="6" y="6" width="24" height="24" rx="3"/><path d="M11 15h14l-4-4M25 21H11l4 4"/></svg></div>

<div class="abs skill" style="left:148px;top:2810px"><h3>Engaging</h3><p>Nam libero tempore, cum soluta nobis</p></div>
<div class="abs skill-icon" style="left:586px;top:2801px;background:var(--green)"><svg width="36" height="36" viewBox="0 0 36 36" fill="none" stroke="#fff" stroke-width="2.4"><rect x="5" y="7" width="26" height="18" rx="2"/><path d="M14 31h8M18 25v6"/><circle cx="18" cy="15" r="3"/><path d="M12 22c1-3 3-4 6-4s5 1 6 4"/></svg></div>

<!-- Blog -->
<section class="abs blog" role="img" aria-label="Soft blurred office background"></section>
<h2 class="abs section-title display blog-title">Blog &amp; Articles</h2>

<article class="abs card card-main">
  <div class="photo" role="img" aria-label="Photo of a smiling call centre agent wearing a headset with colleagues"></div>
  <div class="meta">
    <div class="date"><div class="m">MAR</div><div class="d">20</div></div>
    <div><h4>Sed ut perspiciatis unde omnis iste natus</h4><p>Nemo enim ipsam voluptatem quia voluptas sit aspernatur aut odit aut fugit, sed quia conse quuntur magni dolores</p></div>
  </div>
</article>
<article class="abs card card-side side-1">
  <div class="photo" role="img" aria-label="Photo of colleagues working together at computers"></div>
  <div class="foot"><h4>Sed ut perspiciatis unde omnis iste natus</h4><svg width="14" height="34" viewBox="0 0 14 34"><path d="M2 2l10 15L2 32" fill="none" stroke="var(--ink)" stroke-width="2"/></svg></div>
</article>
<article class="abs card card-side side-2">
  <div class="photo" role="img" aria-label="Photo of a mentor helping a colleague at a laptop"></div>
  <div class="foot"><h4>Sed ut perspiciatis unde omnis iste natus</h4><svg width="14" height="34" viewBox="0 0 14 34"><path d="M2 2l10 15L2 32" fill="none" stroke="var(--ink)" stroke-width="2"/></svg></div>
</article>

<!-- Footer -->
<footer class="abs footer"></footer>
<h2 class="abs contact-title display">Contact us</h2>
<div class="abs field" style="top:4005px">Name</div>
<div class="abs field" style="top:4071px">Phone</div>
<a class="abs btn submit">Submit</a>
<div class="abs footer-brand"><div class="brand-name">VERDANT</div><div class="brand-sub">CONSULTING</div></div>
<div class="abs footer-rule"></div>
<p class="abs copyright">COPYRIGHTS &nbsp;2021 VERDANT.</p>

</body>
</html>
```